business cards and stationary for Fall Protection Company
For construction and Industrial Safety
business cards and stationary for Fall Protection Company - Industrial Supplies
Creative Brief
Modern
Gerald Pennworth
President
2418 N. Birchmont Avenue Compton, CA 90374-2916
gpennworth@ropvexa.com
Ropvexa.com
Want a very clean, crisp look that's a little edgy, too. See www.ropvexa.com and catalog (http://cdn.ropvexa.com/catalogbook_2013/HTML/RV_CatalogBook_2013.html) for current look/feel We are currently using the following fonts: Helvetica Eurostile Lt Std Neuropolitical However, you may use others as long as they compliment our current look/feel You may, but are not required to include our Tag line: "Fall Protection. Precision Engineered."
jlorropvexa jlorropvexa
Would like to see some variations in the way contact information is called out - So far, there are a lot of icons. Would also like to see with just a letter, spelled out or abbreviations - Toll Free: Tel: Customer Service FAX: E-mail: Web:
Also, we prefer square corners rather than die cut.
Qundo Qundo
See the website and catalog for certain accents that we have been using - the squares with arrows, or just the arrows, background grids - we're more straight lines than swooshes

```html
<!DOCTYPE html>
<html lang="en">
<head>
<meta charset="utf-8">
<title>Ropvexa Business Card</title>
<link href="https://fonts.googleapis.com/css2?family=Roboto+Condensed:wght@300;400;700&family=Open+Sans:wght@400;600&display=swap" rel="stylesheet">
<style>
  :root {
    --bg-top: #e6e6e6;
    --bg-bottom: #bdbdbd;
    --card: #ffffff;
    --steel: #5d7fa3;
    --ink: #333333;
    --muted: #6b6b6b;
  }
  * { box-sizing: border-box; margin: 0; padding: 0; }
  html, body { width: 1200px; height: 946px; overflow: hidden; }
  body {
    background: linear-gradient(160deg, var(--bg-top), var(--bg-bottom));
    font-family: "Open Sans", Arial, sans-serif;
    color: var(--ink);
    position: relative;
  }
  .card {
    position: absolute;
    left: 250px;
    width: 700px;
    height: 400px;
    background: var(--card);
    border-radius: 22px;
    box-shadow: 0 14px 30px rgba(0,0,0,0.18);
  }
  .card-back { top: 48px; }
  .card-front { top: 500px; }

  /* back */
  .back-mark {
    position: absolute; left: 0; right: 0; top: 150px;
    display: flex; justify-content: center; align-items: center; gap: 18px;
  }
  .back-mark .square { width: 46px; height: 46px; background: var(--steel); }
  .back-mark .wordmark {
    font-family: "Roboto Condensed", Arial, sans-serif;
    font-weight: 700; font-size: 64px; letter-spacing: 4px; color: var(--steel);
  }
  .social { position: absolute; right: 40px; bottom: 34px; display: flex; gap: 26px; }
  .social-item { display: flex; align-items: center; gap: 7px; font-size: 13px; color: var(--muted); }
  .social-item .square { width: 16px; height: 16px; background: var(--steel); }

  /* front */
  .brand { position: absolute; left: 48px; top: 46px; width: 250px; }
  .brand-row { display: flex; align-items: center; gap: 10px; }
  .brand-row .square { width: 26px; height: 26px; background: var(--steel); }
  .brand-name {
    font-family: "Roboto Condensed", Arial, sans-serif;
    font-weight: 700; font-size: 40px; letter-spacing: 2px; color: var(--ink);
  }
  .tagline { font-size: 11px; color: var(--muted); margin-top: 4px; }

  .identity {
    position: absolute; left: 322px; top: 52px;
    border-left: 4px solid var(--ink); padding-left: 14px;
  }
  .person-name {
    font-family: "Roboto Condensed", Arial, sans-serif;
    font-weight: 400; font-size: 34px; letter-spacing: 2px;
    text-transform: uppercase; color: var(--steel); line-height: 1.1;
  }
  .person-title { font-size: 16px; color: var(--muted); margin-top: 2px; }

  .contacts { position: absolute; left: 54px; top: 170px; display: flex; flex-direction: column; gap: 26px; }
  .contact-row { display: flex; align-items: center; gap: 16px; }
  .contact-row svg { width: 38px; height: 38px; fill: var(--ink); flex: none; }
  .contact-lines { border-left: 4px solid var(--ink); padding-left: 14px; font-size: 17px; line-height: 1.35; }
</style>
</head>
<body>
  <section class="card card-back" aria-label="Business card, back">
    <div class="back-mark">
      <div class="square"></div>
      <div class="wordmark">ROPVEXA</div>
    </div>
    <div class="social">
      <div class="social-item"><span class="square"></span>/ropvexa</div>
      <div class="social-item"><span class="square"></span>/ropvexa</div>
    </div>
  </section>

  <section class="card card-front" aria-label="Business card, front">
    <div class="brand">
      <div class="brand-row">
        <div class="square"></div>
        <div class="brand-name">ROPVEXA</div>
      </div>
      <div class="tagline">Fall Protection. Precision Engineered.</div>
    </div>

    <div class="identity">
      <div class="person-name">Gerald Pennworth</div>
      <div class="person-title">Managing Director</div>
    </div>

    <div class="contacts">
      <div class="contact-row">
        <svg viewBox="0 0 40 40" aria-hidden="true">
          <circle cx="15" cy="12" r="7"/>
          <path d="M2 34c0-8 6-13 13-13s13 5 13 13z"/>
          <circle cx="29" cy="14" r="5"/>
          <path d="M30 21c5 0 9 4 9 11h-8c0-4-1-8-4-10z"/>
        </svg>
        <div class="contact-lines">012 555 0147<br>083 555 0192</div>
      </div>
      <div class="contact-row">
        <svg viewBox="0 0 40 40" aria-hidden="true">
          <path d="M20 2c-7 0-12 5-12 12 0 9 12 24 12 24s12-15 12-24c0-7-5-12-12-12zm0 17a5 5 0 1 1 0-10 5 5 0 0 1 0 10z"/>
        </svg>
        <div class="contact-lines">2418 N. Birchmont Avenue<br>Compton, CA 90374-2916</div>
      </div>
      <div class="contact-row">
        <svg viewBox="0 0 40 40" aria-hidden="true">
          <path fill-rule="evenodd" d="M20 2a18 18 0 1 0 0 36 18 18 0 0 0 0-36zm0 3c2 2 4 6 4.5 12h-9C16 11 18 7 20 5zm-4 .8C14 9 13 13 12.6 17H5.3A15 15 0 0 1 16 5.8zm8 0A15 15 0 0 1 34.7 17h-7.3C27 13 26 9 24 5.8zM5.3 20h7.3c.3 4 1.4 8 3.4 11.2A15 15 0 0 1 5.3 20zm10.2 0h9c-.5 6-2.5 10-4.5 12-2-2-4-6-4.5-12zm11.9 0h7.3A15 15 0 0 1 24 31.2c2-3.2 3.1-7.2 3.4-11.2z"/>
        </svg>
        <div class="contact-lines">gpennworth@ropvexa.com<br>www.ropvexa.com</div>
      </div>
    </div>
  </section>
</body>
</html>
```